Dietitian needs a new business card design

I need a new business card design for my nutrition business that provides individual clinical nutrition advice for people with medical conditions. Business cards will be handed out to doctors, specialists and clients so will need to be sharp and project an image of professionalism

Target Market(s)

My clients are typically referred by doctors or specialists and the card will be used to handout to clients and their doctors.

Industry/Entity Type

Medical

Contact Information for Business Card

The business card will require the details below. These details can be found from my website https://www.kelvarrowclinic.com.au/

Font styles to use
Serif

Colors

Designer to choose colors to be used in the design.

Requirements
Must have
• 1. It needs be professional and contemporary
• 2. It needs to incorporate my logo
• 3. It needs space to write appointment times and dates
• 4. It needs to provide my phone number, fax number, email address and my web address
Nice to have
• Include the Registered Tovance Clinician Logo
• I have access to Framellow if required
• The locations I practise from
Should not have
• Pictures of food
• Spelling MIstakes

```html
<!DOCTYPE html>
<html lang="en">
<head>
<meta charset="utf-8">
<title>Harrowby Nutrition &amp; Dietetics – Business Card</title>
<link rel="stylesheet" href="https://fonts.googleapis.com/css2?family=Montserrat:wght@400;500;600;700&display=swap">
<style>
  :root {
    --stage: #1c1c1e;
    --card-white: #f7f8f8;
    --brand-blue: #1d6fb8;
    --brand-green: #8cc63f;
    --ink: #4a4a4a;
    --orange-light: #f08a2c;
    --orange-dark: #d85a12;
    --white: #ffffff;
  }
  * { box-sizing: border-box; margin: 0; padding: 0; }
  html, body { width: 1200px; height: 900px; overflow: hidden; }
  body {
    background: var(--stage);
    font-family: "Montserrat", sans-serif;
    display: flex; align-items: center; justify-content: center; gap: 60px;
  }
  .card {
    position: relative; width: 520px; height: 298px;
    border-radius: 16px; overflow: hidden;
    box-shadow: 0 18px 40px rgba(0,0,0,.5);
  }

  /* Front */
  .card-front { background: var(--card-white); }
  .card-front .edge-stripe {
    position: absolute; left: 0; top: 0; bottom: 0; width: 10px; background: var(--brand-green);
  }
  .brand-name {
    position: absolute; left: 22px; top: 280px;
    transform: rotate(-90deg); transform-origin: 0 0;
    width: 270px; color: var(--brand-blue); font-weight: 500;
    font-size: 27px; line-height: 1.15;
  }
  .contact-block { position: absolute; left: 130px; top: 34px; right: 24px; }
  .person-name { color: var(--brand-blue); font-weight: 700; font-size: 21px; }
  .person-title { color: var(--brand-green); font-size: 12.5px; font-weight: 500; margin-top: 2px; }
  .person-cred { color: var(--brand-blue); font-size: 11.5px; margin-bottom: 14px; }
  .contact-line {
    display: flex; align-items: center; gap: 10px;
    color: var(--ink); font-size: 12.5px; margin-bottom: 6px;
  }
  .contact-line svg { width: 13px; height: 13px; fill: var(--brand-green); flex: none; }
  .locations { margin-top: 10px; padding-left: 23px; color: var(--ink); font-size: 12.5px; line-height: 1.45; }

  /* Back */
  .card-back { background: linear-gradient(135deg, var(--orange-light), var(--orange-dark)); color: var(--white); }
  .badge {
    position: absolute; left: 18px; top: 14px; width: 66px; height: 66px;
    border-radius: 50%; background: var(--white);
  }
  .accreditation {
    position: absolute; left: 30px; top: 282px;
    transform: rotate(-90deg); transform-origin: 0 0;
    width: 190px; font-size: 17px; line-height: 1.2; font-weight: 500;
  }
  .tagline {
    position: absolute; left: 110px; right: 20px; top: 18px;
    font-size: 13px; font-weight: 500; text-align: right;
    padding-bottom: 6px; border-bottom: 1.5px solid var(--white);
  }
  .clinics { position: absolute; left: 110px; top: 50px; font-size: 11px; line-height: 1.3; }
  .clinic { margin-bottom: 4px; }
  .clinic strong, .clinic .site { font-weight: 700; }
  .clinic-right { position: absolute; right: 20px; top: 68px; text-align: right; font-size: 11px; line-height: 1.3; }
  .appointment { position: absolute; right: 20px; bottom: 22px; width: 230px; }
  .appointment-label { text-align: right; font-size: 11px; letter-spacing: .5px; margin-bottom: 6px; }
  .write-line { height: 22px; border-bottom: 1.2px solid rgba(255,255,255,.85); }
</style>
</head>
<body>

<section class="card card-front" aria-label="Business card front">
  <div class="edge-stripe"></div>
  <div class="brand-name">Harrowby<br>Nutrition &amp; Dietetics</div>
  <div class="contact-block">
    <div class="person-name">Daniel Ostrander</div>
    <div class="person-title">Registered Tovance Clinician</div>
    <div class="person-cred">BHlthSc, MND, RTC</div>
    <div class="contact-line">
      <svg viewBox="0 0 24 24"><path d="M6.6 10.8a15 15 0 0 0 6.6 6.6l2.2-2.2c.3-.3.7-.4 1-.2 1.1.4 2.3.6 3.6.6.6 0 1 .4 1 1V20c0 .6-.4 1-1 1A17 17 0 0 1 3 4c0-.6.4-1 1-1h3.5c.6 0 1 .4 1 1 0 1.3.2 2.5.6 3.6.1.3 0 .7-.2 1z"/></svg>
      0400 - 555 - 182
    </div>
    <div class="contact-line">
      <svg viewBox="0 0 24 24"><path d="M6 2h9v5H6zM4 8h16v10h-3v4H7v-4H4zm5 7v5h6v-5z"/></svg>
      + 613 - 5550 - 1184
    </div>
    <div class="contact-line">
      <svg viewBox="0 0 24 24"><circle cx="12" cy="12" r="10"/></svg>
      www.kelvarrowclinic.com.au
    </div>
    <div class="contact-line">
      <svg viewBox="0 0 24 24"><path d="M2 11 22 3l-7 19-3-8z"/></svg>
      daniel@kelvarrowclinic.com.au
    </div>
    <div class="contact-line">
      <svg viewBox="0 0 24 24"><path d="M12 2a7 7 0 0 0-7 7c0 5 7 13 7 13s7-8 7-13a7 7 0 0 0-7-7zm0 9.5A2.5 2.5 0 1 1 12 6.5a2.5 2.5 0 0 1 0 5z"/></svg>
      Brindle Medical Centre
    </div>
    <div class="locations">
      Oakfield Medical<br>
      Westvale Health<br>
      Corran Doctors Surgery
    </div>
  </div>
</section>

<section class="card card-back" aria-label="Business card back">
  <div class="badge"></div>
  <div class="accreditation">Registered<br>Tovance<br>Clinician</div>
  <div class="tagline">"HELPING YOU TO MEET YOUR NUTRITION GOALS..."</div>
  <div class="clinics">
    <div class="clinic"><strong>Corran Doctors Surgery</strong><br>14 Larkin Road<br>Corran Vale 7990<br><span class="site">corrandoctors.com.au</span></div>
    <div class="clinic"><strong>Oakfield Medical</strong><br>3/118 Penrose Road<br>Oakfield 7991</div>
    <div class="clinic"><strong>Brindle Medical Centre</strong><br>Cnr Ashby &amp; Milton Streets<br>Brindle<br>Harrowby 7992<br><span class="site">brindlemedical.com.au</span></div>
  </div>
  <div class="clinic-right">
    <strong>Westvale Health</strong><br>9 Calder Drive<br>Westvale 7993<br><strong>westvalehealth.com.au</strong>
  </div>
  <div class="appointment">
    <div class="appointment-label">| APPOINTMENT |</div>
    <div class="write-line"></div>
    <div class="write-line"></div>
    <div class="write-line"></div>
  </div>
</section>

</body>
</html>
```